Business Card Vespalor - Accounting firm

Hi my friend.
I'm coming back to you to see if it would be possible for you to make a modern and minimalist business card design.
In shades of blue like the great logo you offered me.
The ideal is a modern and aesthetic business card.
The goal is to give a professional effect to the first exchanges.
Renewal and innovation in the accounting world !!
I thank you !!
Good evening to you

Target Market(s)

Young, dynamic and sensitive to marketing

Industry/Entity Type

Finance And Accounting

Contact Information for Business Card

Company logo and name. Last name, First name, Phone number, email address, company address, website.

Font styles to use
Sans Serif

Requirements
Must have
• The ideal is a modern and aesthetic business card.

Mentions to include: Company logo and name. Last name, First name, Phone number, email address, company address, website.
Nice to have
• The goal is to give a professional effect to the first exchanges.
Should not have
• Simplistic or childish design

```html
<!DOCTYPE html>
<html lang="en">
<head>
<meta charset="UTF-8">
<title>Vespalor – Business Card</title>
<link href="https://fonts.googleapis.com/css2?family=Quicksand:wght@500;600;700&family=Josefin+Sans:wght@600&display=swap" rel="stylesheet">
<style>
  :root {
    --page-bg: #cfd0d1;
    --card-navy: #1a3878;
    --card-navy-deep: #142c66;
    --accent-teal: #3fd0b4;
    --accent-blue: #2b8fd8;
    --text-white: #ffffff;
    --frame-line: rgba(120, 160, 230, 0.28);
  }
  * { margin: 0; padding: 0; box-sizing: border-box; }
  html, body {
    width: 1200px;
    height: 675px;
    overflow: hidden;
    background: var(--page-bg);
  }
  .canvas {
    width: 1200px;
    height: 675px;
    display: flex;
    align-items: center;
    justify-content: center;
    gap: 60px;
  }
  .card {
    position: relative;
    width: 520px;
    height: 298px;
    border-radius: 22px;
    background: linear-gradient(135deg, var(--card-navy-deep) 0%, var(--card-navy) 55%, var(--card-navy-deep) 100%);
    box-shadow: 0 14px 30px rgba(20, 30, 60, 0.25);
    overflow: hidden;
    color: var(--text-white);
    font-family: "Quicksand", sans-serif;
  }
  .wordmark {
    display: flex;
    align-items: center;
    gap: 12px;
    font-family: "Quicksand", sans-serif;
    font-weight: 700;
    color: var(--text-white);
    letter-spacing: 0.5px;
  }
  .wordmark-square {
    background: var(--accent-teal);
    border-radius: 4px;
  }

  /* Front: contact side */
  .card-front .wordmark {
    position: absolute;
    left: 44px;
    top: 62px;
    font-size: 32px;
  }
  .card-front .wordmark-square { width: 26px; height: 26px; }
  .divider {
    position: absolute;
    left: 0;
    right: 36px;
    top: 176px;
    height: 2px;
    background: linear-gradient(90deg, var(--accent-blue), var(--accent-teal));
  }
  .person {
    position: absolute;
    right: 44px;
    top: 128px;
    text-align: right;
  }
  .person-name {
    font-family: "Josefin Sans", sans-serif;
    font-weight: 600;
    font-size: 28px;
    letter-spacing: 1px;
    color: var(--accent-teal);
    line-height: 1;
  }
  .person-role {
    font-size: 12px;
    font-weight: 600;
    margin-top: 2px;
  }
  .contact-list {
    position: absolute;
    list-style: none;
    font-size: 13px;
    font-weight: 600;
  }
  .contact-list li {
    display: flex;
    align-items: center;
    gap: 9px;
    margin-bottom: 8px;
  }
  .contact-list svg { width: 12px; height: 12px; flex-shrink: 0; }
  .contact-left { left: 44px; top: 196px; }
  .contact-right { right: 90px; top: 220px; }

  /* Back: brand side */
  .card-back .frame {
    position: absolute;
    inset: 22px;
    border: 1.5px solid var(--frame-line);
    border-radius: 18px;
  }
  .card-back .frame-inner {
    position: absolute;
    left: 70px; top: -40px;
    width: 300px; height: 260px;
    border: 1.5px solid var(--frame-line);
    border-radius: 40px;
  }
  .card-back .wordmark {
    position: absolute;
    left: 50%;
    top: 50%;
    transform: translate(-50%, -50%);
    font-size: 46px;
  }
  .card-back .wordmark-square { width: 36px; height: 36px; border-radius: 6px; }
</style>
</head>
<body>
<main class="canvas">
  <section class="card card-front" aria-label="Business card front">
    <div class="wordmark"><span class="wordmark-square"></span>Vespalor</div>
    <div class="person">
      <div class="person-name">NAME</div>
      <div class="person-role">Designation</div>
    </div>
    <div class="divider"></div>
    <ul class="contact-list contact-left">
      <li>
        <svg viewBox="0 0 12 12"><path d="M6 0.5a4 4 0 0 0-4 4c0 3 4 7 4 7s4-4 4-7a4 4 0 0 0-4-4zm0 5.6a1.6 1.6 0 1 1 0-3.2 1.6 1.6 0 0 1 0 3.2z" fill="var(--accent-teal)"/></svg>
        Address
      </li>
      <li>
        <svg viewBox="0 0 12 12"><path d="M2.6 1h2l1 2.6-1.3 1a6 6 0 0 0 3.1 3.1l1-1.3 2.6 1v2A1.3 1.3 0 0 1 9.7 11 9 9 0 0 1 1 2.3 1.3 1.3 0 0 1 2.6 1z" fill="var(--accent-teal)"/></svg>
        Phone number
      </li>
    </ul>
    <ul class="contact-list contact-right">
      <li>
        <svg viewBox="0 0 12 12"><rect x="0.5" y="2" width="11" height="8" rx="1.2" fill="var(--accent-teal)"/><path d="M1 2.8l5 3.6 5-3.6" stroke="var(--card-navy)" stroke-width="1" fill="none"/></svg>
        E-mail
      </li>
      <li>
        <svg viewBox="0 0 12 12"><circle cx="6" cy="6" r="5" fill="var(--accent-teal)"/><path d="M1 6h10M6 1c-2.2 2.6-2.2 7.4 0 10M6 1c2.2 2.6 2.2 7.4 0 10" stroke="var(--card-navy)" stroke-width="0.8" fill="none"/></svg>
        Website
      </li>
    </ul>
  </section>

  <section class="card card-back" aria-label="Business card back">
    <div class="frame"></div>
    <div class="frame-inner"></div>
    <div class="wordmark"><span class="wordmark-square"></span>Vespalor</div>
  </section>
</main>
</body>
</html>
```